Build a Web page - Dorin Vaughtley Homes, LLC - a custom home builder

We are a custom home builder in Wisconsin. Need a basic web page with a home page, About Us, Contact info, Gallery, and Testimonials page. Gallery will probably have sub-pages and each will have about ten pictures or less. I already own the domain and have web hosting through Wix, I just need the site built. Once the page is built I should be able to do the upkeep on it myself. If I need to add pictures or whatever.
Updates

Project Deadline Extended
Reason: I am still looking through designs and will select soon - thank you!

Target Market(s)

Gen X and Millennials who are looking to build a home. Custom built homes - not generic spec homes.

Industry/Entity Type

Home Builder

Number of Pages Required

5+ page

Font styles to use
Sans Serif

Colors
ffffff
ec1f27
000000
9d9d9d

Requirements
Must have
• I have no idea if I want coded or in coded. I'm not sure of the difference and why I would want one over the other.
Nice to have
• We like the following colors - red, black, gray, white.
Should not have
• not a big fan of clip art like hammers, tape measures, etc. Must look professional.

```html
<!DOCTYPE html>
<html lang="en">
<head>
<meta charset="utf-8">
<title>Dorin Vaughtley Homes, LLC – Custom Home Builder</title>
<link href="https://fonts.googleapis.com/css2?family=Jost:wght@400;500;600&family=Lato:wght@400;700&display=swap" rel="stylesheet">
<style>
:root{
  --red:#a50f16;
  --red-bright:#c3161f;
  --red-dark:#7d0a10;
  --black:#111;
  --ink:#333;
  --grey:#9d9d9d;
  --grey-dark:#6d6d6d;
  --grey-bar:#6b6b6b;
  --light:#f1f1f1;
  --white:#fff;
}
*{box-sizing:border-box;margin:0;padding:0}
html,body{width:1200px;height:3502px;overflow:hidden}
body{font-family:"Lato",sans-serif;color:var(--ink);background:var(--white);position:relative}
.abs{position:absolute}
h2,.heading{font-family:"Jost",sans-serif;font-weight:500;text-transform:uppercase}
.wordmark{font-family:"Jost",sans-serif;font-weight:600;color:var(--red);text-transform:uppercase;line-height:1.05;text-align:center;letter-spacing:1px}

/* header */
.topbar{left:0;top:0;width:1200px;height:51px;background:var(--grey-bar)}
.topbar .item{top:8px;height:35px;display:flex;align-items:center;color:#fff;font-size:19px;gap:12px}
.topbar .ico{width:35px;height:35px;background:var(--red);display:flex;align-items:center;justify-content:center}
.header{left:0;top:51px;width:1200px;height:108px;background:#fff;box-shadow:0 2px 4px rgba(0,0,0,.1)}
.logo-box{left:77px;top:12px;width:152px;height:140px;background:#fff;border:6px solid #8a8a8a;display:flex;align-items:center;justify-content:center;box-shadow:0 2px 6px rgba(0,0,0,.2)}
.logo-box .wordmark{font-size:20px}
.nav{right:88px;top:94px;display:flex;font-size:16px;text-transform:uppercase;font-family:"Jost",sans-serif}
.nav a{color:var(--ink);text-decoration:none;padding:0 24px;border-left:1px solid #ddd}
.nav a:first-child{border:none;color:var(--red)}

/* hero */
.hero{left:0;top:159px;width:1200px;height:481px;background:linear-gradient(180deg,#7fa6d0 0%,#c2d6e8 35%,#8a8f7a 60%,#4e6b35 100%)}
.hero-arrow{top:340px;width:40px;height:40px;background:rgba(0,0,0,.6);display:flex;align-items:center;justify-content:center}
.hero-caption{left:0;top:584px;width:1200px;height:56px;background:rgba(40,40,40,.75);color:#fff;text-align:center;font-family:"Jost",sans-serif;font-size:27px;line-height:56px;letter-spacing:1.5px;text-transform:uppercase}

/* separators */
.sep{display:flex;align-items:center;gap:8px}
.sep i{display:block;height:2px;background:#bbb}
.sep b{display:block;width:18px;height:9px;background:repeating-linear-gradient(110deg,#aaa 0 3px,transparent 3px 6px)}

/* welcome */
.welcome h2{left:79px;top:694px;width:590px;white-space:nowrap;font-size:29px;color:var(--red)}
.welcome h2 span{color:var(--ink)}
.welcome p{left:79px;top:778px;width:572px;font-size:15.5px;line-height:26px;color:#444}
.btn{background:var(--grey-dark);color:#fff;font-size:14px;font-weight:700;display:flex;align-items:center;justify-content:center}
.video{left:689px;top:700px;width:430px;height:327px;background:#e8e8e8;box-shadow:0 3px 8px rgba(0,0,0,.25)}
.video .screen{left:0;top:0;width:430px;height:285px;background:linear-gradient(180deg,#b9c3cc,#cfc7b6 55%,#6f7f4f)}
.video .bar{left:0;top:285px;width:430px;height:42px;background:linear-gradient(#f4f4f4,#d4d4d4)}

/* why choose us */
.why{left:0;top:1086px;width:1200px;height:521px;background:linear-gradient(180deg,#2a2320,#1b1716 60%,#231c18)}
.feature h3{font-family:"Jost",sans-serif;font-weight:500;color:#fff;font-size:20px}
.feature p{color:#ddd;font-size:13.5px;line-height:19px;margin-top:4px}
.feature.left{text-align:right;width:260px}
.feature.right{width:260px}
.center-logo{left:479px;top:1315px;width:245px;height:219px;background:#fff;border:8px solid #cfcfcf;outline:3px solid #fff;outline-offset:-20px;display:flex;align-items:center;justify-content:center}
.center-logo .wordmark{font-size:30px}

/* gallery */
.gallery h2{left:0;top:1648px;width:1200px;text-align:center;font-size:36px;color:var(--red)}
.gallery h2 span{color:var(--ink)}
.tab{top:1756px;height:42px;color:#fff;font-size:17px;font-weight:700;display:flex;align-items:center;justify-content:center;background:var(--grey-bar);transform:skewX(-8deg)}
.tab span{transform:skewX(8deg)}
.tab.active{background:var(--red)}
.grid{left:79px;top:1826px;width:1042px;display:grid;grid-template-columns:repeat(4,1fr);gap:6px}
.grid div{height:202px;position:relative}
.tile-overlay{position:absolute;inset:0;background:rgba(20,20,20,.72);color:#fff;text-align:center;display:flex;flex-direction:column;align-items:center;justify-content:center}
.tile-overlay strong{font-family:"Jost",sans-serif;font-size:26px;font-weight:500;margin-top:10px}
.tile-overlay small{font-size:14px;line-height:18px;width:190px}

/* testimonials */
.testimonials{left:0;top:2312px;width:1200px;height:490px;background:linear-gradient(135deg,#b3121b,#8c0b11 50%,#a3111a)}
.card{top:2447px;width:332px;height:266px;background:#fff;box-shadow:0 3px 8px rgba(0,0,0,.3)}
.card .avatar{left:21px;top:23px;width:91px;height:75px;background:linear-gradient(#d9d9d9,#a8a8a8)}
.card .name{left:134px;top:38px;color:var(--red);font-family:"Jost",sans-serif;font-size:18px}
.card .stars{left:134px;top:64px;color:var(--red);font-size:13px;letter-spacing:2px}
.card .quote{left:21px;top:120px;width:290px;font-size:13.5px;line-height:21px;color:#444}
.dots{left:0;top:2745px;width:1200px;display:flex;justify-content:center;gap:8px}
.dots i{width:11px;height:11px;border:2px solid #fff;border-radius:50%}
.dots i.on{background:#fff}

/* map */
.map{left:0;top:2802px;width:1200px;height:275px;background:linear-gradient(180deg,#e9ecdf,#f0eee6 50%,#e5e8dc)}
.map-marker{left:730px;top:2847px;width:82px;height:74px;background:#fff;border:3px solid #8a8a8a;display:flex;align-items:center;justify-content:center}
.map-marker .wordmark{font-size:10px}

/* contact */
.contact{left:0;top:3077px;width:1200px;height:374px;background:linear-gradient(180deg,#f3f3f3,#e9e9e9)}
.form-title{left:85px;top:3211px;font-size:18px;color:#222}
.field{background:#fff;border:1px solid #ddd;font-size:12px;color:#555;padding:0 10px;display:flex;align-items:center}
.field.area{align-items:flex-start;padding-top:12px}
.info h4{font-family:"Jost",sans-serif;font-weight:600;color:var(--red);font-size:15px;text-transform:uppercase}
.info p{font-size:13px;color:#555;line-height:18px;margin-top:4px}
.info svg{position:absolute;left:-34px;top:0}

/* footer */
.footer{left:0;top:3451px;width:1200px;height:51px;background:var(--red-dark);color:#fff;font-size:12px}
.footer .copy{left:79px;top:18px}
.footer-logo{left:849px;top:3426px;width:80px;height:76px;background:#fff;border:3px solid #8a8a8a;display:flex;align-items:center;justify-content:center}
.footer-logo .wordmark{font-size:10px}
.social{right:78px;top:14px;display:flex;gap:5px}
.social i{width:26px;height:26px;border:1px solid rgba(255,255,255,.7);display:block}
</style>
</head>
<body>

<!-- header -->
<div class="abs topbar">
  <div class="abs item" style="left:655px">
    <span class="ico"><svg width="18" height="18" viewBox="0 0 24 24"><path fill="#fff" d="M6.6 10.8a15 15 0 0 0 6.6 6.6l2.2-2.2c.3-.3.7-.4 1-.2 1.1.4 2.3.6 3.6.6.6 0 1 .4 1 1V20c0 .6-.4 1-1 1A17 17 0 0 1 3 4c0-.6.4-1 1-1h3.5c.6 0 1 .4 1 1 0 1.3.2 2.5.6 3.6.1.3 0 .7-.2 1z"/></svg></span>
    123 456 7890
  </div>
  <div class="abs item" style="left:838px">
    <span class="ico"><svg width="18" height="14" viewBox="0 0 20 14"><rect x="1" y="1" width="18" height="12" fill="none" stroke="#fff" stroke-width="2"/><path d="M1 1l9 7 9-7" fill="none" stroke="#fff" stroke-width="2"/></svg></span>
    info@dorinvaughtleyhomes.com
  </div>
</div>
<div class="abs header"></div>
<div class="abs logo-box"><div class="wordmark">Dorin<br>Vaughtley<br>Homes</div></div>
<nav class="abs nav">
  <a href="#">Home</a><a href="#">About Us</a><a href="#">Gallery</a><a href="#">Testimonials</a><a href="#">Contact Us</a>
</nav>

<!-- hero -->
<div class="abs hero" role="img" aria-label="Photo of a two-storey custom home with stone garage front and green lawn"></div>
<div class="abs hero-arrow" style="left:8px"><svg width="14" height="18" viewBox="0 0 14 18"><path d="M11 2L3 9l8 7" fill="none" stroke="#fff" stroke-width="3"/></svg></div>
<div class="abs hero-arrow" style="left:1152px"><svg width="14" height="18" viewBox="0 0 14 18"><path d="M3 2l8 7-8 7" fill="none" stroke="#fff" stroke-width="3"/></svg></div>
<div class="abs hero-caption">We are a custom home builder in Wisconsin, USA</div>

<!-- welcome -->
<section class="welcome">
  <h2 class="abs">Welcome to Dorin <span>Vaughtley Homes</span></h2>
  <div class="abs sep" style="left:79px;top:748px"><b></b><i style="width:540px"></i></div>
  <p class="abs">Lorem ipsum dolor sit amet, consectetuer adipiscing elit, sed diam nonummy nibh euismod tincidunt ut laoreet dolore magna aliquam erat volutpat. Ut wisi enim ad minim veniam, quis nostrud exerci tation ullamcorper suscipit lobortis nisl ut aliquip ex ea commodo consequat. Duis autem vel eum iriure dolor in hendrerit in vulputate velit esse molestie consequat, vel illum dolore eu feugiat nulla facilisis at vero eros et accumsan et iusto odio dignissim qui blandit praesent luptatum zzril delenit augue duis dolore te feugait nulla facilisi.</p>
  <div class="abs btn" style="left:79px;top:980px;width:117px;height:38px">Read More &raquo;</div>
  <div class="abs video">
    <div class="abs screen" role="img" aria-label="Video still of a finished home with patio and backyard"></div>
    <svg class="abs" style="left:185px;top:112px" width="60" height="60" viewBox="0 0 60 60"><circle cx="30" cy="30" r="27" fill="rgba(255,255,255,.35)" stroke="#fff" stroke-width="3"/><path d="M24 18l18 12-18 12z" fill="#fff"/></svg>
    <div class="abs bar">
      <svg class="abs" style="left:10px;top:10px" width="410" height="22" viewBox="0 0 410 22">
        <rect x="0" y="2" width="22" height="18" fill="#fff" stroke="#aaa"/><rect x="7" y="6" width="3" height="10" fill="#333"/><rect x="13" y="6" width="3" height="10" fill="#333"/>
        <rect x="48" y="2" width="38" height="18" fill="#fff" stroke="#aaa"/><path d="M60 6l-7 5 7 5zM74 6l7 5-7 5z" fill="#333"/>
        <rect x="100" y="9" width="200" height="4" rx="2" fill="#bbb"/><rect x="100" y="9" width="150" height="4" rx="2" fill="#4a8fd4"/><circle cx="250" cy="11" r="5" fill="#fff" stroke="#888"/>
        <rect x="232" y="-6" width="38" height="10" fill="#3a6e9e"/>
        <path d="M325 8h4l5-4v14l-5-4h-4z" fill="#333"/><rect x="342" y="9" width="50" height="4" rx="2" fill="#4a8fd4"/>
      </svg>
    </div>
  </div>
</section>

<!-- why choose us -->
<section class="abs why" role="img" aria-label="Dark photo of a finished living room interior"></section>
<h2 class="abs heading" style="left:0;top:1138px;width:1200px;text-align:center;color:#fff;font-size:38px">Why Choose Us</h2>
<div class="abs sep" style="left:478px;top:1201px"><i style="width:108px;background:#888"></i><b></b><i style="width:108px;background:#888"></i></div>
<div class="abs" style="left:0;top:1236px;width:1200px;text-align:center;color:#fff;font-size:19px">Lorem ipsum dolor sit amet, consectetuer adipiscing elit</div>

<svg class="abs" style="left:0;top:1300px" width="1200" height="250" viewBox="0 0 1200 250">
  <g stroke="#777" stroke-width="1.5" fill="none">
    <path d="M392 55H455l24 20"/><path d="M392 188H455l24-20"/>
    <path d="M808 55H745l-21 20"/><path d="M808 188H745l-21-20"/>
  </g>
  <g fill="var(--red-bright)"><circle cx="390" cy="55" r="5"/><circle cx="390" cy="188" r="5"/><circle cx="810" cy="55" r="5"/><circle cx="810" cy="188" r="5"/></g>
  <g transform="translate(323,34)" fill="none" stroke="#fff" stroke-width="2.5"><path d="M2 2h18l8 8v30H2z"/><path d="M8 14h12M8 22h12"/><circle cx="24" cy="32" r="6"/></g>
  <g transform="translate(310,170)" fill="#fff"><path d="M2 14h6v14H2zM10 14l6-12c3 0 4 2 3 5l-2 6h9c2 0 3 2 2 4l-3 10c-1 1-2 2-3 2H10z"/><circle cx="44" cy="16" r="11" fill="none" stroke="#fff" stroke-width="2.5"/><text x="44" y="22" font-size="16" font-family="Lato" font-weight="700" text-anchor="middle">$</text></g>
  <g transform="translate(822,36)" fill="#fff"><circle cx="12" cy="8" r="6"/><circle cx="28" cy="5" r="6"/><circle cx="44" cy="8" r="6"/><path d="M0 28c0-9 6-13 12-13s12 4 12 13zM16 25c0-9 6-13 12-13s12 4 12 13zM32 28c0-9 6-13 12-13s12 4 12 13z"/></g>
  <g transform="translate(832,160)" fill="#fff"><circle cx="15" cy="14" r="13"/><circle cx="15" cy="14" r="7" fill="none" stroke="#222" stroke-width="2"/><path d="M7 24l-4 14 7-3 4 6 3-12zM23 24l4 14-7-3-4 6-3-12z"/></g>
</svg>

<div class="abs feature left" style="left:46px;top:1328px"><h3>Certified Experience</h3><p>Lorem ipsum dolor sit amet,<br>consectetuer Lorem ipsum...[+]</p></div>
<div class="abs feature left" style="left:46px;top:1472px"><h3>Competitive Pricing</h3><p>Lorem ipsum dolor sit amet,<br>consectetuer Lorem ipsum...[+]</p></div>
<div class="abs feature right" style="left:885px;top:1328px"><h3>Highly Professionals</h3><p>Lorem ipsum dolor sit amet,<br>consectetuer Lorem ipsum...[+]</p></div>
<div class="abs feature right" style="left:885px;top:1472px"><h3>100% Satisfaction</h3><p>Lorem ipsum dolor sit amet,<br>consectetuer Lorem ipsum...[+]</p></div>
<div class="abs center-logo"><div class="wordmark">Dorin<br>Vaughtley<br>Homes</div></div>

<!-- gallery -->
<section class="gallery">
  <h2 class="abs">Project <span>Gallery</span></h2>
  <div class="abs sep" style="left:478px;top:1706px"><i style="width:108px"></i><b></b><i style="width:108px"></i></div>
  <div class="abs tab active" style="left:110px;width:182px"><span>View All</span></div>
  <svg class="abs" style="left:191px;top:1797px" width="18" height="10"><path d="M0 0h18L9 9z" fill="var(--red)"/></svg>
  <div class="abs tab" style="left:311px;width:179px"><span>Annie</span></div>
  <div class="abs tab" style="left:509px;width:182px"><span>Cassey</span></div>
  <div class="abs tab" style="left:710px;width:182px"><span>Dr</span></div>
  <div class="abs tab" style="left:911px;width:179px"><span>Tara</span></div>
  <div class="abs grid">
    <div role="img" aria-label="Kitchen with wood cabinets" style="background:linear-gradient(#6b4a30,#3b2a1c)">
      <div class="tile-overlay">
        <svg width="40" height="40" viewBox="0 0 40 40" fill="none" stroke="#fff" stroke-width="2.5"><path d="M4 14V4h10M4 4l12 12M36 14V4H26M36 4L24 16M4 26v10h10M4 36l12-12M36 26v10H26M36 36L24 24"/></svg>
        <strong>ANNIE</strong>
        <small>Duis autem vel eum iriure dolor in hendrerit in vulputate.</small>
      </div>
    </div>
    <div role="img" aria-label="Hallway kitchen with oak cabinets" style="background:linear-gradient(135deg,#d8d2c6,#8a5e38)"></div>
    <div role="img" aria-label="Living room with stone fireplace and ceiling fan" style="background:linear-gradient(#e3e5e4,#8f857a)"></div>
    <div role="img" aria-label="Family room with fireplace and windows" style="background:linear-gradient(135deg,#efe6d6,#9c6a45)"></div>
    <div role="img" aria-label="Tiled fireplace with wood mantel" style="background:linear-gradient(135deg,#8a5a33,#c8b59c)"></div>
    <div role="img" aria-label="Wooden deck in a backyard" style="background:linear-gradient(#dfe3e6,#7a4f3a 60%,#6b7f4a)"></div>
    <div role="img" aria-label="Kitchen island with bar stools" style="background:linear-gradient(135deg,#b77f45,#5a3b24)"></div>
    <div role="img" aria-label="Bathroom with white vanity" style="background:linear-gradient(#f4f2ee,#c7c0b4)"></div>
  </div>
</section>

<!-- testimonials -->
<section class="abs testimonials" role="img" aria-label="Red low-poly background"></section>
<h2 class="abs heading" style="left:0;top:2343px;width:1200px;text-align:center;color:#fff;font-size:37px">Client Testimonials</h2>
<div class="abs sep" style="left:370px;top:2402px"><i style="width:216px;background:rgba(255,255,255,.6)"></i><b style="background:repeating-linear-gradient(110deg,#fff 0 3px,transparent 3px 6px)"></b><i style="width:216px;background:rgba(255,255,255,.6)"></i></div>

<div class="abs card" style="left:79px">
  <div class="abs avatar" role="img" aria-label="Client portrait"></div>
  <div class="abs name">Rafael Moreno</div><div class="abs stars">★★★★★</div>
  <p class="abs quote">Lorem ipsum dolor sit amet, consectetuer ading elit, sed diam nonummy nibh euismod tincidunt ut laoreet dolore magna aliquam erat volutpat. Ut wisi enim ad minim veniam, quis nostrud exerci tation ullamcorper</p>
</div>
<div class="abs card" style="left:432px">
  <div class="abs avatar" role="img" aria-label="Client portrait"></div>
  <div class="abs name">Daniel Marsh</div><div class="abs stars">★★★★★</div>
  <p class="abs quote">Lorem ipsum dolor sit amet, consectetuer ading elit, sed diam nonummy nibh euismod tincidunt ut laoreet dolore magna aliquam erat volutpat. Ut wisi enim ad minim veniam, quis nostrud exerci tation ullamcorper</p>
</div>
<div class="abs card" style="left:787px">
  <div class="abs avatar" role="img" aria-label="Client portrait"></div>
  <div class="abs name">Bianca O'Neill</div><div class="abs stars">★★★★★</div>
  <p class="abs quote">Lorem ipsum dolor sit amet, consectetuer ading elit, sed diam nonummy nibh euismod tincidunt ut laoreet dolore magna aliquam erat volutpat. Ut wisi enim ad minim veniam, quis nostrud exerci tation ullamcorper</p>
</div>
<div class="abs dots"><i></i><i></i><i class="on"></i><i></i></div>

<!-- map -->
<div class="abs map" role="img" aria-label="Road map of the surrounding region showing the office location"></div>
<div class="abs map-marker"><div class="wordmark">Dorin<br>Vaughtley<br>Homes</div></div>
<svg class="abs" style="left:711px;top:2944px" width="20" height="28" viewBox="0 0 20 28"><path d="M10 0a10 10 0 0 1 10 10c0 7-10 18-10 18S0 17 0 10A10 10 0 0 1 10 0z" fill="var(--red)"/><circle cx="10" cy="10" r="4" fill="#fff"/></svg>

<!-- contact -->
<section class="abs contact"></section>
<h2 class="abs heading" style="left:0;top:3104px;width:1200px;text-align:center;font-size:37px;color:var(--red)">Contact <span style="color:var(--ink)">Us</span></h2>
<div class="abs sep" style="left:478px;top:3163px"><i style="width:108px"></i><b></b><i style="width:108px"></i></div>
<div class="abs form-title">Please Fill Your Details We will Get Back to You Soon</div>
<div class="abs field" style="left:79px;top:3260px;width:255px;height:37px">Name</div>
<div class="abs field" style="left:79px;top:3314px;width:255px;height:37px">Email</div>
<div class="abs field" style="left:79px;top:3368px;width:255px;height:37px">Phone</div>
<div class="abs field area" style="left:357px;top:3260px;width:341px;height:93px">How We Can Help You?</div>
<div class="abs btn" style="left:357px;top:3369px;width:98px;height:35px">Submit &raquo;</div>
<div class="abs" style="left:772px;top:3200px;width:1px;height:230px;background:#d6d6d6"></div>

<div class="abs info" style="left:853px;top:3212px">
  <svg width="16" height="22" viewBox="0 0 20 28"><path d="M10 0a10 10 0 0 1 10 10c0 7-10 18-10 18S0 17 0 10A10 10 0 0 1 10 0z" fill="var(--red)"/><circle cx="10" cy="10" r="4" fill="#fff"/></svg>
  <h4>Address Information</h4>
  <p>DORIN VAUGHTLEY HOMES<br>12345 Lo 10th Iriure, Molestie, AB 01234</p>
</div>
<div class="abs info" style="left:853px;top:3296px">
  <svg width="20" height="14" viewBox="0 0 20 14"><rect width="20" height="14" fill="var(--red)"/><path d="M1 1l9 7 9-7" fill="none" stroke="#fff" stroke-width="2"/></svg>
  <h4>Email</h4>
  <p>info@dorinvaughtleyhomes.com</p>
</div>
<div class="abs info" style="left:853px;top:3358px">
  <svg width="18" height="18" viewBox="0 0 24 24"><path fill="var(--red)" d="M6.6 10.8a15 15 0 0 0 6.6 6.6l2.2-2.2c.3-.3.7-.4 1-.2 1.1.4 2.3.6 3.6.6.6 0 1 .4 1 1V20c0 .6-.4 1-1 1A17 17 0 0 1 3 4c0-.6.4-1 1-1h3.5c.6 0 1 .4 1 1 0 1.3.2 2.5.6 3.6.1.3 0 .7-.2 1z"/></svg>
  <h4>Call Us</h4>
  <p>123 456 7890</p>
</div>

<!-- footer -->
<footer class="abs footer">
  <div class="abs copy">Copyright © 2017 Dorin Vaughtley Homes. All Rights Reserved.</div>
  <div class="abs social"><i></i><i></i><i></i><i></i></div>
</footer>
<div class="abs footer-logo"><div class="wordmark">Dorin<br>Vaughtley<br>Homes</div></div>

</body>
</html>
```